Webdesign für Verkauf von Stoffen
Zielgruppe
Palmtuche ist schon seit 15 Jahren auf den Märkten unterwegs und verkauft seine hochwertigen Stoffe vor Ort. Nun muss die Webseite ein neuen Look bekommen, sie sollte modern und locker wirken. Die Webseite ist eher für Privatkunden und hat jetzt noch keine Shop Möglichkeit, die wird aber intrigiert mit einzelnen Produkten.
Aufgabenstellung
Logo gibt es noch nicht, soll erstmal nur in Schriftform bleiben, ansonsten gibt es keine explizierten Vorgaben

```html
<!DOCTYPE html>
<html lang="de">
<head>
<meta charset="utf-8">
<title>Palm Tuche – Feiner Stich</title>
<link href="https://fonts.googleapis.com/css2?family=Jost:wght@300;400;500;600;700&display=swap" rel="stylesheet">
<style>
:root{
  --navy:#1e2472;
  --navy-deep:#0d1547;
  --gold:#c29a3a;
  --grey:#e3e3e3;
  --line:#5b63a8;
  --white:#fff;
}
*{margin:0;padding:0;box-sizing:border-box}
html,body{width:1200px;height:2250px;overflow:hidden;background:var(--white);font-family:'Jost',sans-serif;color:var(--navy)}
.page{position:relative;width:1200px;height:2250px}
.abs{position:absolute}

/* header */
.brand{left:40px;top:28px;display:flex;align-items:center;gap:10px}
.brand-square{width:34px;height:30px;border:2px solid var(--navy);border-radius:3px}
.brand-name{font-size:20px;font-weight:400;line-height:1;letter-spacing:.2px;color:var(--navy)}
.nav{right:50px;top:0;display:flex;gap:30px;height:87px;align-items:center}
.nav a{font-size:10px;font-weight:600;letter-spacing:1.6px;color:var(--navy);text-decoration:none;position:relative;padding-top:8px}
.nav a.active::before{content:"";position:absolute;left:0;right:0;top:-38px;height:3px;background:var(--gold)}

/* hero */
.hero{left:0;top:87px;width:1200px;height:325px;background:linear-gradient(90deg,#c85a6a,#2f79b8 15%,#e8b73a 28%,#c93a3a 40%,#2aa5b8 55%,#d2453f 68%,#3c8fc4 82%,#7a9b4b)}
.label{background:var(--navy);color:var(--white);display:flex;flex-direction:column;align-items:center;justify-content:center;position:absolute}
.label::before,.label::after{content:"";position:absolute;top:6px;bottom:6px;border-left:1.5px dashed var(--gold)}
.label::before{left:16px}.label::after{right:16px}
.hero-label{left:264px;top:175px;width:673px;height:136px}
.hero-title{font-size:48px;font-weight:400;letter-spacing:.5px;line-height:1}
.hero-tag{color:var(--gold);font-size:24px;font-weight:300;letter-spacing:3px;line-height:1;margin-top:12px}

/* intro */
.intro-title{left:0;width:1200px;top:455px;text-align:center;font-size:29px;font-weight:300;letter-spacing:.3px}
.intro-rule{left:562px;top:501px;width:75px;height:2px;background:var(--gold)}
.intro-text{left:260px;width:680px;top:517px;text-align:center;font-size:17.5px;font-weight:300;line-height:1.35}

/* fabric tiles */
.tile{width:325px;height:227px;border-radius:12px;overflow:hidden}
.tile .label{left:50px;top:96px;width:237px;height:43px;font-size:14px;font-weight:400;letter-spacing:.3px}
.t-linen{left:264px;top:595px;background:linear-gradient(135deg,#cbc4b6,#a59c8a 50%,#d8d1c3)}
.t-canvas{left:614px;top:595px;background:linear-gradient(135deg,#5b586a,#8e8aa0 50%,#b7b3c4)}
.t-sweet{left:264px;top:848px;background:linear-gradient(135deg,#5f7fcc,#2c4da0 55%,#1b3a8a)}
.t-jersey{left:614px;top:848px;background:linear-gradient(135deg,#f7b23a,#f4a21e 55%,#e89618)}

/* social feed */
.feed{left:0;top:1114px;width:1200px;height:366px;background:var(--grey)}
.feed-mark{left:584px;top:1133px;width:32px;height:32px;border:3px solid var(--navy);border-radius:50%}
.feed-frame{left:256px;top:1186px;width:675px;height:222px;background:#f3f3f3}
.feed-img{top:1195px;width:203px;height:203px}
.f1{left:268px;background:linear-gradient(180deg,#d8b7b4,#5a7a5a 40%,#c7487a 70%,#3f6cb3)}
.f2{left:490px;background:linear-gradient(135deg,#3aa5b5,#e07a95 50%,#2f8c9c)}
.f3{left:713px;background:linear-gradient(180deg,#d04a5a,#1c2f8a 50%,#c73b44)}
.follow{left:532px;top:1428px;width:136px;height:30px;border:1.5px solid var(--navy);display:flex;align-items:center;justify-content:center;font-size:12.5px;font-weight:400}

/* dates */
.cal{left:583px;top:1515px}
.dates-title{left:0;width:1200px;top:1567px;text-align:center;font-size:19px;font-weight:500;letter-spacing:.3px}
.dates{left:263px;top:1612px;width:675px}
.row{display:flex;justify-content:space-between;height:77px;padding-top:4px;border-bottom:1px solid var(--line)}
.row .city,.row .day{font-size:18px;font-weight:700;letter-spacing:.3px;line-height:1.3}
.row .addr,.row .time{font-size:18px;font-weight:400;line-height:1.4}
.row .right{text-align:right;padding-right:8px}

/* footer */
.footer{left:0;top:1882px;width:1200px;height:318px;background:radial-gradient(ellipse at 60% 40%,#1f2e7a,#0d1547 70%,#081036)}
.contact{left:263px;top:1954px;color:var(--white);font-size:11.5px;font-weight:600;letter-spacing:.3px}
.contact li{list-style:none;display:flex;align-items:center;height:26px}
.contact .ico{width:26px;display:flex}
.social{left:865px;top:1958px;display:flex;gap:8px}
.social span{width:25px;height:25px;background:var(--white);border-radius:3px}
.legal{left:263px;top:2222px;font-size:13.5px;display:flex;gap:18px}
.legal span{color:var(--navy)}
</style>
</head>
<body>
<div class="page">

  <header>
    <div class="abs brand">
      <div class="brand-square"></div>
      <div class="brand-name">PALM TUCHE</div>
    </div>
    <nav class="abs nav">
      <a class="active">WILLKOMMEN</a><a>STOFFE</a><a>ÜBER MICH</a><a>KONTAKT</a><a>TERMINE</a>
    </nav>
  </header>

  <section>
    <div class="abs hero" role="img" aria-label="Foto bunter Batikstoffe, aufgerollt nebeneinander"></div>
    <div class="label hero-label">
      <div class="hero-title">PALM TUCHE</div>
      <div class="hero-tag">FEINER STICH</div>
    </div>
  </section>

  <section>
    <h1 class="abs intro-title">ELEGANZ KOMMT NIE AUS DER MODE</h1>
    <div class="abs intro-rule"></div>
    <p class="abs intro-text">Palmtuche ist schon seit 15 Jahren auf den Märkten unterwegs und verkauft seine hochwertigen Stoffe vor Ort.</p>

    <div class="abs tile t-linen" role="img" aria-label="Foto von Leinenstoff"><div class="label">LINEN</div></div>
    <div class="abs tile t-canvas" role="img" aria-label="Foto von grauem Strickstoff"><div class="label">CANVAS</div></div>
    <div class="abs tile t-sweet" role="img" aria-label="Foto von blauem Sweatstoff"><div class="label">SWEET</div></div>
    <div class="abs tile t-jersey" role="img" aria-label="Foto von gelbem Jersey"><div class="label">JERSEY</div></div>
  </section>

  <section>
    <div class="abs feed"></div>
    <div class="abs feed-mark"></div>
    <div class="abs feed-frame"></div>
    <div class="abs feed-img f1" role="img" aria-label="Foto bunter Stoffballen am Marktstand"></div>
    <div class="abs feed-img f2" role="img" aria-label="Foto eines gemusterten Pfauenstoffs"></div>
    <div class="abs feed-img f3" role="img" aria-label="Foto eines farbigen Motivstoffs"></div>
    <div class="abs follow">FOLGE MIR</div>
  </section>

  <section>
    <svg class="abs cal" width="34" height="40" viewBox="0 0 34 40">
      <rect x="2" y="6" width="30" height="32" fill="none" stroke="#1e2472" stroke-width="2.5"/>
      <rect x="2" y="6" width="30" height="7" fill="#1e2472"/>
      <rect x="8" y="1" width="3" height="8" fill="#1e2472"/><rect x="23" y="1" width="3" height="8" fill="#1e2472"/>
      <g fill="#1e2472">
        <rect x="7" y="17" width="3" height="3"/><rect x="12" y="17" width="3" height="3"/><rect x="17" y="17" width="3" height="3"/><rect x="22" y="17" width="3" height="3"/>
        <rect x="7" y="23" width="3" height="3"/><rect x="12" y="23" width="3" height="3"/><rect x="17" y="23" width="3" height="3"/><rect x="22" y="23" width="3" height="3"/>
        <rect x="7" y="29" width="3" height="3"/><rect x="12" y="29" width="3" height="3"/><rect x="17" y="29" width="3" height="3"/><rect x="22" y="29" width="3" height="3"/>
      </g>
    </svg>
    <h2 class="abs dates-title">TERMINE / MÄRKTE 2022</h2>
    <div class="abs dates">
      <div class="row"><div><div class="city">HAMBURG-HARBURG</div><div class="addr">21073 Hamburg, Hamburgrer Rathausplatz</div></div><div class="right"><div class="day">SA. 03.09</div><div class="time">10.00-17.00</div></div></div>
      <div class="row"><div><div class="city">PODSTAM</div><div class="addr">14467 Neuer Lustgarten, Lange Brücke / Breite Straße</div></div><div class="right"><div class="day">SO. 04.09</div><div class="time">10.00-17.00</div></div></div>
      <div class="row"><div><div class="city">BERLIN</div><div class="addr">10249 Markthalle Plenzlauer Berg, Ostseestraße 12</div></div><div class="right"><div class="day">SO. 16.10</div><div class="time">10.00-17.00</div></div></div>
    </div>
  </section>

  <footer>
    <div class="abs footer" role="img" aria-label="Foto von dunkelblauem Samtstoff"></div>
    <ul class="abs contact">
      <li><span class="ico"><svg width="13" height="13" viewBox="0 0 13 13"><circle cx="6.5" cy="3.5" r="3" fill="#fff"/><path d="M1 13c0-4 2.5-5.5 5.5-5.5S12 9 12 13z" fill="#fff"/></svg></span>Matthias Velden</li>
      <li><span class="ico"></span>PALM TUCHE - FEINER STICH</li>
      <li><span class="ico"><svg width="11" height="14" viewBox="0 0 11 14"><path d="M5.5 0a5.5 5.5 0 0 0-5.5 5.5C0 9 5.5 14 5.5 14S11 9 11 5.5A5.5 5.5 0 0 0 5.5 0z" fill="#fff"/><circle cx="5.5" cy="5.5" r="2" fill="#0d1547"/></svg></span>Lindenhofweg 24</li>
      <li><span class="ico"></span>13409 Berlin</li>
      <li><span class="ico"><svg width="13" height="13" viewBox="0 0 13 13"><path d="M2 0l3 3-1.5 2a8 8 0 0 0 4.5 4.5L10 8l3 3-2 2C5 13 0 8 0 2z" fill="#fff"/></svg></span>Tel.: 0176/48120937</li>
      <li><span class="ico"><svg width="13" height="10" viewBox="0 0 13 10"><rect width="13" height="10" fill="#fff"/><path d="M0 0l6.5 5L13 0" fill="none" stroke="#0d1547" stroke-width="1.3"/></svg></span>palm.tuche@postfach.de</li>
    </ul>
    <div class="abs social"><span></span><span></span></div>
    <div class="abs legal"><span>Impressum</span><span>|</span><span>Datenschutz</span></div>
  </footer>

</div>
</body>
</html>
```